Wireless Internet Service Provider website design

We need a Internet Service Provider website that show the packages that we offer as well as the functionality where customers have the option of clicking on the various packages and be linked to a page where they can sign up for our services.
We need about 10-15 pages.
A. Integrated online store.
B. Live chat.
C. Social media page
My old website. Brindleport.nyc

Example: http://quarrylinknet.com/services/residential/ Added Tuesday, June 7, 2016

Target Market(s)

Residential and small businesses

Industry/Entity Type

Internet

Coding

Coded - Design and coding required

Number of Pages Required

5+ page

Font styles to use
Serif
Sans Serif
Script

Colors
3176b5
85cae6
ffffff

Requirements
Must have
• Online store and live chat, drop down details on pricing from current website
Nice to have
• great design, functional website,

```html
<!DOCTYPE html>
<html lang="en">
<head>
<meta charset="utf-8">
<title>Brindleport Wireless</title>
<link rel="stylesheet" href="https://fonts.googleapis.com/css2?family=Roboto:ital,wght@0,300;0,400;0,500;1,400&family=Exo+2:wght@600&display=swap">
<style>
:root{
  --blue:#3176b5;
  --sky:#85cae6;
  --white:#ffffff;
  --navy:#0d1420;
  --ink:#111821;
  --grey-text:#8a8f96;
  --card:#f0f1f3;
  --deep-blue:#2a67a8;
}
*{margin:0;padding:0;box-sizing:border-box}
html,body{width:1200px;height:2804px;overflow:hidden}
body{font-family:"Roboto",sans-serif;background:var(--white);color:#333;position:relative}
.abs{position:absolute}

/* HERO */
.hero{position:absolute;left:0;top:0;width:1200px;height:678px;
  background:radial-gradient(ellipse at 60% 40%,#2c3644 0%,#141a22 55%,#090c11 100%)}
.nav{position:absolute;left:77px;top:22px;width:1046px;height:40px;border-bottom:1px solid rgba(255,255,255,.25);
  display:flex;align-items:flex-start;font-size:16px;color:var(--white);letter-spacing:.3px}
.nav a{color:var(--white);text-decoration:none;margin-right:32px;padding:0 16px 0 16px;height:40px;position:relative}
.nav a:first-child{padding-left:16px}
.nav .active{color:var(--sky)}
.nav .active::after{content:"";position:absolute;left:0;right:0;bottom:-2px;height:3px;background:var(--sky)}
.nav .cart{margin-left:auto;display:flex;gap:10px;font-size:18px}
.brand{position:absolute;left:0;width:1200px;top:320px;text-align:center;font-size:44px;font-weight:500;color:#9aa3ad;
  display:flex;justify-content:center;align-items:center;gap:18px}
.brand .dot{width:34px;height:34px;border-radius:50%;background:var(--sky)}
.headline{position:absolute;left:0;width:1200px;top:405px;text-align:center;font-family:"Exo 2",sans-serif;
  font-weight:600;font-size:42px;line-height:52px;color:var(--white);letter-spacing:1px}
.scroll-down{position:absolute;left:577px;top:538px;width:46px;height:46px;border:2px solid var(--sky);border-radius:50%}

.services{position:absolute;left:0;top:678px;width:1200px;height:186px;background:var(--blue)}
.service{position:absolute;top:0;width:300px;text-align:center;color:var(--white);font-size:19px;line-height:26px}
.service .badge{position:absolute;left:85px;top:-66px;width:130px;height:130px;border-radius:50%;background:var(--white);
  border:8px solid var(--sky);display:flex;align-items:center;justify-content:center}
.service p{position:absolute;top:80px;width:300px}
.service .rule{position:absolute;left:128px;top:146px;width:44px;height:2px;background:var(--white)}

/* ABOUT */
.globe{position:absolute;left:95px;top:945px;width:390px;height:360px;border-radius:50%/50%;
  background:radial-gradient(circle at 40% 35%,#cfe6fb 0%,#5a9ee4 45%,#1c56a8 85%,#e9edf2 86%,#ffffff 100%)}
.about-title{position:absolute;left:606px;top:925px;font-size:38px;color:var(--blue);font-weight:400}
.about-lead{position:absolute;left:606px;top:985px;width:520px;font-size:15px;line-height:28px;color:var(--grey-text)}
.feature{position:absolute;left:552px;display:flex;align-items:flex-start;gap:22px}
.feature .ic{width:58px;height:58px;border-radius:50%;border:3px solid var(--blue);display:flex;align-items:center;justify-content:center;flex:none}
.feature h4{font-weight:400;font-size:17px;color:#4a4f55;margin-top:12px}
.feature p{font-size:14px;line-height:24px;color:var(--grey-text);margin-top:6px;width:420px}

/* PLANS */
.plans{position:absolute;left:0;top:1355px;width:1200px;height:702px;
  background:radial-gradient(ellipse at 70% 60%,#1d4a86 0%,#0f2548 45%,#070d1a 100%)}
.plans-title{position:absolute;left:0;width:1200px;top:56px;text-align:center;font-size:40px;color:var(--white);font-weight:400}
.tabs{position:absolute;left:280px;top:150px;width:640px;height:46px;border-bottom:1px solid rgba(255,255,255,.35);display:flex;justify-content:center;gap:32px;font-size:19px}
.tabs .on{color:var(--sky)}
.tabs .off{color:var(--white)}
.plan{position:absolute;top:225px;width:250px;height:415px;background:var(--card)}
.plan .head{height:103px;background:var(--sky);color:var(--white);font-style:italic;font-size:22px;line-height:30px;text-align:center;padding-top:20px}
.plan .icon{margin:22px auto 0;width:70px;height:62px;display:flex;align-items:center;justify-content:center}
.plan .price{text-align:center;font-size:32px;color:#555;margin-top:12px}
.plan .term{text-align:center;font-style:italic;color:var(--blue);font-size:18px;margin-top:8px}
.plan .name{text-align:center;color:#555;font-size:20px;margin-top:8px}
.plan .more{display:block;margin:24px auto 0;width:168px;height:56px;border-radius:28px;background:var(--blue);color:var(--white);
  font-size:20px;line-height:56px;text-align:center}
.plan.featured{background:rgba(20,45,85,.55);border:2px solid rgba(133,202,230,.35);height:420px}
.plan.featured .head{background:var(--deep-blue)}
.plan.featured .price,.plan.featured .name{color:var(--white)}
.plan.featured .blurb{text-align:center;color:var(--white);font-size:14px;line-height:25px;padding:16px 22px 0}

/* TESTIMONIALS */
.say-title{position:absolute;left:0;width:1200px;top:2112px;text-align:center;font-size:40px;color:var(--blue)}
.quote{position:absolute;top:2200px;width:520px;height:130px}
.quote .avatar{position:absolute;left:0;top:0;width:124px;height:124px;border-radius:50%;border:4px solid #e2e4e6;
  background:radial-gradient(circle,#c9b7a5 0%,#8c7a6a 100%)}
.quote .mark{position:absolute;left:134px;top:0;font-size:46px;color:#7fb2de;font-family:Georgia,serif;line-height:46px}
.quote blockquote{position:absolute;left:170px;top:12px;width:320px;font-size:14px;line-height:29px;color:var(--grey-text)}
.quote cite{position:absolute;left:170px;top:108px;font-style:normal;font-size:16px;color:var(--blue)}

/* FOOTER */
.footer{position:absolute;left:0;top:2387px;width:1200px;height:417px;background:linear-gradient(#0b111a,#111a26)}
.col-title{position:absolute;top:50px;font-size:20px;color:var(--white)}
.field{position:absolute;left:77px;width:334px;height:46px;background:var(--blue);color:var(--white);font-size:14px;line-height:46px;padding-left:16px}
.btn{position:absolute;width:334px;height:46px;background:var(--white);color:var(--blue);font-size:20px;line-height:46px;text-align:center;letter-spacing:1px}
.chatbox{position:absolute;left:434px;top:95px;width:332px;height:150px;background:var(--blue);color:var(--white);font-size:14px;padding:14px 16px}
.touch{position:absolute;left:798px;width:325px;display:flex;gap:24px;color:var(--white);font-size:14px;line-height:24px;padding-bottom:18px;border-bottom:1px solid rgba(133,202,230,.45)}
.touch svg{flex:none;margin-top:2px}
.copy{position:absolute;left:77px;top:2741px;width:1046px;border-top:1px solid rgba(133,202,230,.4);text-align:center;color:var(--white);font-size:14px;padding-top:24px}
.copy b{color:var(--sky);font-weight:400}
</style>
</head>
<body>

<header class="hero">
  <nav class="nav">
    <a class="active">HOME</a><a>WHY BRINDLEPORT</a><a>PLANS &amp; PACKAGES</a><a>MY ACCOUNT</a><a>GALLERY</a><a>CONTACT</a>
    <span class="cart">
      <svg width="24" height="20" viewBox="0 0 24 20"><path d="M1 2h4l3 11h12l3-8H7" fill="none" stroke="#85cae6" stroke-width="2"/><circle cx="10" cy="17" r="2" fill="#85cae6"/><circle cx="18" cy="17" r="2" fill="#85cae6"/></svg>
      Shopping cart 0
    </span>
  </nav>
  <div class="brand"><span class="dot"></span>Brindleport Wireless</div>
  <h1 class="headline">LOCALLY OWN, RELIABLE, SUPER<br>FAST INTRNET</h1>
  <div class="scroll-down">
    <svg width="42" height="42" viewBox="0 0 42 42"><path d="M13 17l8 8 8-8" fill="none" stroke="#85cae6" stroke-width="2"/></svg>
  </div>
</header>

<section class="services">
  <div class="service" style="left:95px">
    <div class="badge"><svg width="64" height="64" viewBox="0 0 64 64" fill="#3176b5"><rect x="10" y="8" width="20" height="48"/><rect x="34" y="20" width="6" height="6"/><rect x="34" y="32" width="6" height="6"/><rect x="34" y="44" width="6" height="6"/><path d="M40 23h10v30H40" fill="none" stroke="#3176b5" stroke-width="3"/><rect x="14" y="14" width="4" height="4" fill="#fff"/><rect x="22" y="14" width="4" height="4" fill="#fff"/><rect x="14" y="26" width="4" height="4" fill="#fff"/><rect x="22" y="26" width="4" height="4" fill="#fff"/><rect x="14" y="38" width="4" height="4" fill="#fff"/><rect x="22" y="38" width="4" height="4" fill="#fff"/></svg></div>
    <p>RESIDENTIAL INTERNET<br>ACCESS</p><span class="rule"></span>
  </div>
  <div class="service" style="left:450px">
    <div class="badge"><svg width="64" height="64" viewBox="0 0 64 64"><path d="M12 22a22 22 0 0 0 30 30z" fill="#3176b5"/><path d="M27 37l10-10M26 50l-6 10h16l-6-10" stroke="#3176b5" stroke-width="3" fill="none"/><path d="M40 16a10 10 0 0 1 8 8M40 8a18 18 0 0 1 16 16" stroke="#3176b5" stroke-width="3" fill="none"/></svg></div>
    <p>BUSINESS INTERNET<br>ACCESS</p><span class="rule"></span>
  </div>
  <div class="service" style="left:805px">
    <div class="badge"><svg width="64" height="64" viewBox="0 0 64 64" fill="none" stroke="#3176b5" stroke-width="3"><circle cx="32" cy="32" r="24"/><path d="M8 32h48M32 8v48"/><rect x="24" y="16" width="18" height="32" rx="3" fill="#fff"/></svg></div>
    <p>UNLIMITED INTERNET<br>USAGE</p><span class="rule"></span>
  </div>
</section>

<section class="about">
  <div class="globe" role="img" aria-label="Illustration of a blue globe with a network cable plugged into it"></div>
  <h2 class="about-title">ABOUT BRINDLEPORT WIRELESS</h2>
  <p class="about-lead">Brindleport wireless is a highly reputable company, which is aiming at providing high quality internet access and phone services...</p>
  <div class="feature" style="top:1062px">
    <span class="ic"><svg width="30" height="30" viewBox="0 0 30 30" fill="none" stroke="#3176b5" stroke-width="2.5"><circle cx="15" cy="13" r="7"/><path d="M5 15a10 10 0 0 1 20 0M7 26h16"/></svg></span>
    <div><h4>CUSTOMER SUPPORT CENTER</h4><p>Reliable and Amicable Customer Support Services at Your Doorstep 24/7, 365</p></div>
  </div>
  <div class="feature" style="top:1157px">
    <span class="ic"><svg width="30" height="30" viewBox="0 0 30 30" fill="none" stroke="#3176b5" stroke-width="3"><circle cx="15" cy="15" r="5"/><path d="M15 3v5M15 22v5M3 15h5M22 15h5M6.5 6.5l3.5 3.5M20 20l3.5 3.5M6.5 23.5l3.5-3.5M20 10l3.5-3.5"/></svg></span>
    <div><h4>EQUIPMENT OPTIONS</h4></div>
  </div>
  <div class="feature" style="top:1231px">
    <span class="ic"><svg width="30" height="30" viewBox="0 0 30 30" fill="#3176b5"><rect x="4" y="13" width="5" height="13"/><path d="M11 13l5-9c2 0 3 1 3 3l-1 5h7c2 0 3 2 2 4l-3 9c-1 1-2 1-3 1H11z"/></svg></span>
    <div><h4>CUSTOMER GUARANTEE</h4></div>
  </div>
</section>

<section class="plans">
  <h2 class="plans-title">OUR PLANS &amp; PACKAGES</h2>
  <div class="tabs"><span class="on">Residential Internet Access</span><span class="off">Business Internet Access</span></div>

  <article class="plan" style="left:77px">
    <div class="head">5 Mbps Download<br>Speed</div>
    <div class="icon"><svg width="70" height="50" viewBox="0 0 70 50"><rect x="6" y="18" width="28" height="20" fill="#3176b5"/><circle cx="52" cy="30" r="14" fill="#3176b5"/><path d="M20 10a22 22 0 0 1 32 4" stroke="#5cb85c" stroke-width="4" fill="none"/></svg></div>
    <div class="price">$39.99</div><div class="term">Mo/1 Year</div><div class="name">Brindleport Simplicity</div>
    <a class="more">KNOW MORE</a>
  </article>

  <article class="plan" style="left:344px">
    <div class="head">10 Mbps Download<br>Speed</div>
    <div class="icon"><svg width="50" height="50" viewBox="0 0 50 50" stroke="#3176b5" stroke-width="3"><path d="M25 6v8M25 36v8M6 25h8M36 25h8M12 12l5 5M33 33l5 5M12 38l5-5M33 17l5-5"/><circle cx="25" cy="25" r="4" fill="#3176b5"/></svg></div>
    <div class="price">$49.95</div><div class="term">Mo/1 Year</div><div class="name">Brindleport Value Pak</div>
    <a class="more">KNOW MORE</a>
  </article>

  <article class="plan featured" style="left:606px">
    <div class="head">50 Mbps Download<br>Speed</div>
    <div class="icon"><svg width="70" height="70" viewBox="0 0 70 70"><rect width="70" height="70" fill="#fff"/><path d="M20 30a22 22 0 0 1 30 0M26 37a13 13 0 0 1 18 0" stroke="#3176b5" stroke-width="4" fill="none"/><circle cx="35" cy="45" r="4" fill="#3176b5"/></svg></div>
    <div class="price">$89.99</div><div class="name">Brindleport Action Pak</div>
    <p class="blurb">With super-fast download speeds of 50 Mbps, this is the all-in plan for anyone whose..</p>
  </article>

  <article class="plan" style="left:873px">
    <div class="head">25 Mbps Download<br>Speed</div>
    <div class="icon"><svg width="56" height="56" viewBox="0 0 56 56" fill="none" stroke="#2aa0b8" stroke-width="4"><path d="M10 28a18 18 0 0 1 30-13M46 28a18 18 0 0 1-30 13"/><path d="M28 18l-6 26M28 18l6 26" stroke="#3176b5" stroke-width="3"/></svg></div>
    <div class="price">$69.99</div><div class="term">Mo/1 Year</div><div class="name">Brindleport Super- Pak</div>
    <a class="more">KNOW MORE</a>
  </article>
</section>

<section class="testimonials">
  <h2 class="say-title">WHAT OUR CLIENT SAY</h2>
  <figure class="quote" style="left:77px">
    <div class="avatar" role="img" aria-label="Portrait photo of a smiling client"></div>
    <span class="mark">&ldquo;</span>
    <blockquote>"By far the best customer service I have ever received from an Internet service provider. Brindleport stands above the rest.." <span style="color:#7fb2de">&rdquo;</span></blockquote>
    <cite>Dara Whitfield</cite>
  </figure>
  <figure class="quote" style="left:617px">
    <div class="avatar" role="img" aria-label="Portrait photo of a smiling client"></div>
    <span class="mark">&ldquo;</span>
    <blockquote>" Thanks for your great service. I love my inte - rnet and your quick response to my ques - tions and concerns. I would .." <span style="color:#7fb2de">&rdquo;</span></blockquote>
    <cite>Malik Orvend</cite>
  </figure>
</section>

<footer class="footer">
  <h3 class="col-title" style="left:80px;font-weight:400">CONTACT FORM</h3>
  <h3 class="col-title" style="left:434px;font-weight:400">LIVE CHAT</h3>
  <h3 class="col-title" style="left:798px;font-weight:400">GET IN TOUCH</h3>

  <div class="field" style="top:95px">Name :</div>
  <div class="field" style="top:148px">Phone :</div>
  <div class="field" style="top:200px">Email :</div>
  <div class="btn" style="left:77px;top:254px">SUBMIT</div>

  <div class="chatbox">Start chat with us :</div>
  <div class="btn" style="left:434px;top:254px;width:332px">SEND</div>

  <div class="touch" style="top:97px">
    <svg width="22" height="28" viewBox="0 0 22 28" fill="none" stroke="#fff" stroke-width="2"><path d="M11 26s9-9 9-15a9 9 0 0 0-18 0c0 6 9 15 9 15z"/><circle cx="11" cy="11" r="3"/></svg>
    <span>BRINDLEPORT WIRELESS<br>P O Box 527140 Brooklyn NY<br>11290</span>
  </div>
  <div class="touch" style="top:200px">
    <svg width="22" height="22" viewBox="0 0 22 22" fill="none" stroke="#fff" stroke-width="2"><path d="M3 2h5l2 5-3 2a12 12 0 0 0 6 6l2-3 5 2v5c-10 1-18-7-17-17z"/></svg>
    <span>866-555-0142</span>
  </div>
  <div class="touch" style="top:260px;border-bottom:none">
    <svg width="22" height="18" viewBox="0 0 22 18" fill="none" stroke="#fff" stroke-width="2"><rect x="1" y="1" width="20" height="16"/><path d="M1 1l10 9 10-9"/></svg>
    <span>support@brindleport.nyc</span>
  </div>
</footer>
<p class="copy">&copy;<b>BRINDLEPORT WIRELESS</b> - 2016 All rights reserved.</p>

</body>
</html>
```